RK Teardown business cards v.2 first was me

So the ones in the picture are my original cards that I came up with. 😅however I kinda messed up on two things, I missed spelled my name it should be Marcello Vantosa as well as the email should be Marcellov@brightlanecrews.com. I would like to clean this card up and also make it pop! Something that people would remember me by and that screams DEMOLITION. As well as a card that give you a feeling of loyalty and trust. I would also like to change and remove junk hauling and add full demolition to replace it. These cards worked for a little while but I cant make that my image while handing these out. I would also like to only put down that we are located in Canyon Ridge, CA, 92601 instead of the address on the card. Also if we can have a line that states Licensed, Bonded, & Insured. With out License # 4837215

Target Market(s)

Contractors and Home owners

Industry/Entity Type

Construction specialist in Demolition

Contact Information for Business Card

R Teardown Selective Demolition & Full Demolition Kitchens AD Preparation Bathrooms Sheds Interiors & Exteriors Demo Digging And Much More Marcellllo Vantosa Owner our city state and zip

Font styles to use
Serif
Sans Serif
Decorative

Colors
0054AA
0677BA
7BADD7
CADEEF
E8F1F8
0094D4
00A9DD
6FCCEA
C7EBF8
E9F6FB

Requirements
Must have
• License# 4837215
Nice to have
• Trying to go with a blue and white color scheme
Should not have
• Building construction

```html
<!DOCTYPE html>
<html lang="en">
<head>
<meta charset="utf-8">
<title>R Teardown Business Cards</title>
<link href="https://fonts.googleapis.com/css2?family=Lato:wght@400;700;900&display=swap" rel="stylesheet">
<style>
  :root {
    --bg: #2b2b2d;
    --brand-blue: #0f4c97;
    --ink: #111111;
    --muted: #2f2f2f;
    --paper: #ffffff;
  }
  * { margin: 0; padding: 0; box-sizing: border-box; }
  html, body {
    width: 1200px; height: 875px; overflow: hidden;
    background: var(--bg);
    font-family: "Lato", sans-serif;
  }
  .stage { position: relative; width: 1200px; height: 875px; }
  .card {
    position: absolute; top: 288px;
    width: 520px; height: 298px;
    border-radius: 22px;
    overflow: hidden;
  }
  /* Front */
  .card--front { left: 50px; background: var(--paper); }
  .front-logo {
    position: absolute; left: 60px; top: 58px;
    display: flex; align-items: center; gap: 14px;
  }
  .front-logo__square { width: 44px; height: 44px; background: var(--brand-blue); }
  .front-logo__name {
    font-weight: 900; font-size: 50px; letter-spacing: 1px;
    color: var(--brand-blue); text-transform: uppercase; line-height: 1;
  }
  .front-license {
    position: absolute; left: 250px; top: 118px;
    font-weight: 900; font-size: 17px; color: var(--ink); letter-spacing: .5px;
  }
  .front-headline {
    position: absolute; left: 36px; top: 186px;
    font-weight: 900; font-size: 19.5px; color: var(--brand-blue);
    letter-spacing: .4px; text-transform: uppercase;
  }
  .front-services {
    position: absolute; left: 36px; top: 216px;
    font-size: 12.5px; color: var(--muted); text-transform: uppercase;
    letter-spacing: .5px; line-height: 1.55;
  }
  .dot { display: inline-block; width: 6px; height: 6px; border-radius: 50%;
    background: var(--brand-blue); vertical-align: middle; margin: 0 4px 2px; }

  /* Back */
  .card--back { left: 630px; background: var(--brand-blue); color: var(--paper); }
  .back-logo {
    position: absolute; right: 32px; top: 30px;
    display: flex; align-items: center; gap: 10px;
  }
  .back-logo__square { width: 30px; height: 30px; background: var(--paper); border-radius: 4px; }
  .back-logo__name { font-weight: 900; font-size: 26px; text-transform: uppercase; letter-spacing: .5px; }
  .back-rule { position: absolute; left: 30px; right: 30px; top: 112px; height: 2px; background: var(--paper); }
  .back-name {
    position: absolute; left: 30px; top: 138px;
    font-weight: 900; font-size: 28px; letter-spacing: .8px; text-transform: uppercase;
  }
  .back-role { position: absolute; left: 32px; top: 174px; font-size: 15px; }
  .back-rule--short { top: 200px; right: auto; width: 210px; }
  .contact-list { position: absolute; left: 30px; top: 212px; list-style: none; font-size: 13px; line-height: 22px; }
  .contact-list li { display: flex; align-items: center; gap: 8px; }
  .contact-list svg { width: 13px; height: 13px; flex: none; }
  .back-credentials {
    position: absolute; right: 30px; bottom: 30px; text-align: right;
    font-size: 12.5px; letter-spacing: .4px; line-height: 1.4; text-transform: uppercase;
  }
  .back-credentials strong { font-weight: 900; }
</style>
</head>
<body>
<main class="stage">
  <section class="card card--front" aria-label="Business card front">
    <div class="front-logo">
      <span class="front-logo__square"></span>
      <span class="front-logo__name">R Teardown</span>
    </div>
    <p class="front-license">LICENSE# 4837215</p>
    <h2 class="front-headline">Selective Demolition &amp; Full Demolition</h2>
    <p class="front-services">
      Kitchens <span class="dot"></span> ADU Preparation <span class="dot"></span> Bathrooms <span class="dot"></span> Sheds<br>
      Interiors and Exteriors Demo <span class="dot"></span> Digging and Much More
    </p>
  </section>

  <section class="card card--back" aria-label="Business card back">
    <div class="back-logo">
      <span class="back-logo__square"></span>
      <span class="back-logo__name">R Teardown</span>
    </div>
    <div class="back-rule"></div>
    <h1 class="back-name">Marcello Vantosa</h1>
    <p class="back-role">Owner</p>
    <div class="back-rule back-rule--short"></div>
    <ul class="contact-list">
      <li>
        <svg viewBox="0 0 24 24" fill="#fff"><path d="M6.6 10.8a15.1 15.1 0 0 0 6.6 6.6l2.2-2.2a1 1 0 0 1 1-.25 11.4 11.4 0 0 0 3.6.57 1 1 0 0 1 1 1V20a1 1 0 0 1-1 1A17 17 0 0 1 3 4a1 1 0 0 1 1-1h3.5a1 1 0 0 1 1 1c0 1.25.2 2.45.57 3.57a1 1 0 0 1-.25 1z"/></svg>
        (949)555-0187
      </li>
      <li>
        <svg viewBox="0 0 24 24" fill="#fff"><path d="M2 5h20v14H2z M3.5 6.5 12 13l8.5-6.5" stroke="#0f4c97" stroke-width="1.5"/></svg>
        Marcellov@brightlanecrews.com
      </li>
      <li>
        <svg viewBox="0 0 24 24" fill="#fff"><path d="M12 2a7 7 0 0 0-7 7c0 5 7 13 7 13s7-8 7-13a7 7 0 0 0-7-7zm0 9.5A2.5 2.5 0 1 1 12 6.5a2.5 2.5 0 0 1 0 5z"/></svg>
        Canyon Ridge, CA, 92601
      </li>
    </ul>
    <p class="back-credentials"><strong>Licensed, Bonded, &amp; Insured</strong><br>License# 4837215</p>
  </section>
</main>
</body>
</html>
```